Business Card Design Project

We need business cards for our new business, Veltrano Skyworks. We specialize in aerial videography and photography via drone. Currently we are mainly focusing on real estate videography but will branch into other markets and may even host training classes for flying drones.
Cards should include:
Name
Phone Number
Email Address
Web address
We will need to customize for more than one person and would like those fields to be editable
eps file logos are uploaded now, thanks!
Target Market(s)
Real Estate Agents, hotels, rental agencies and people who have recently purchase drones
Industry/Entity Type
Videography

```html
<!DOCTYPE html>
<html lang="en">
<head>
<meta charset="utf-8">
<title>Veltrano Skyworks — Business Card</title>
<link rel="stylesheet" href="https://fonts.googleapis.com/css2?family=Open+Sans:wght@400;600;700&display=swap">
<style>
  :root {
    --canvas-bg: #e6e6e4;
    --brand-orange: #f2a42e;
    --brand-orange-light: #f9c46a;
    --brand-orange-deep: #eb9a22;
    --charcoal: #3a3a3b;
    --slate: #58585a;
    --white: #ffffff;
    --photo-green: #7f9a5c;
    --photo-earth: #b9a889;
    --photo-sky: #93a7a6;
  }
  * { box-sizing: border-box; margin: 0; padding: 0; }
  html, body {
    width: 1200px; height: 1200px; overflow: hidden;
    background: var(--canvas-bg);
    font-family: "Open Sans", Arial, sans-serif;
  }
  .canvas { position: relative; width: 1200px; height: 1200px; }
  .card {
    position: absolute; top: 232px;
    width: 420px; height: 736px;
    overflow: hidden;
    box-shadow: 0 10px 28px rgba(0,0,0,0.18);
  }
  /* Front */
  .card-front {
    left: 150px;
    background: radial-gradient(ellipse at 50% 40%, var(--brand-orange-light) 0%, var(--brand-orange) 55%, var(--brand-orange-deep) 100%);
    display: flex; flex-direction: column; align-items: center;
  }
  .brand-mark {
    margin-top: 190px;
    width: 150px; height: 150px;
    background: var(--charcoal);
  }
  .brand-name-front {
    margin-top: 42px;
    font-weight: 700; font-size: 33px; letter-spacing: 1px;
    color: var(--charcoal); text-transform: uppercase;
    text-align: center; line-height: 1.15;
  }
  .brand-rule {
    margin-top: 18px; width: 270px; height: 2px;
    background: var(--charcoal); opacity: 0.55;
  }
  .website {
    position: absolute; bottom: 118px; left: 0; right: 0;
    text-align: center;
    font-weight: 700; font-size: 22px; color: var(--charcoal);
  }
  /* Back */
  .card-back { left: 630px; background: var(--slate); }
  .aerial-photo {
    height: 300px;
    background: linear-gradient(160deg, var(--photo-sky) 0%, var(--photo-green) 35%, var(--photo-earth) 60%, var(--photo-green) 100%);
  }
  .brand-name-back {
    margin-top: 34px; text-align: center;
    font-weight: 700; font-size: 30px; letter-spacing: 1px;
    color: var(--white); text-transform: uppercase;
  }
  .brand-rule-back {
    margin: 14px auto 0; width: 250px; height: 2px;
    background: var(--white); opacity: 0.5;
  }
  .person { padding: 54px 0 0 58px; }
  .person-name {
    font-weight: 700; font-size: 24px; color: var(--brand-orange);
    text-transform: uppercase;
  }
  .person-role {
    font-weight: 600; font-size: 22px; color: var(--white); margin-top: 4px;
  }
  .contact-list { list-style: none; margin-top: 26px; }
  .contact-item {
    display: flex; align-items: center; gap: 16px;
    font-weight: 600; font-size: 19px; color: var(--white);
    margin-bottom: 8px;
  }
  .contact-icon { width: 18px; height: 18px; flex: none; fill: var(--brand-orange); }
</style>
</head>
<body>
<main class="canvas">
  <section class="card card-front" aria-label="Card front">
    <div class="brand-mark"></div>
    <h1 class="brand-name-front">Veltrano<br>Skyworks</h1>
    <div class="brand-rule"></div>
    <p class="website">www.veltranoskyworks.com</p>
  </section>

  <section class="card card-back" aria-label="Card back">
    <div class="aerial-photo" role="img" aria-label="Aerial drone photograph of a campus with buildings, roads and green fields"></div>
    <h2 class="brand-name-back">Veltrano Skyworks</h2>
    <div class="brand-rule-back"></div>
    <div class="person">
      <p class="person-name">Marcus Dale</p>
      <p class="person-role">Manager</p>
      <ul class="contact-list">
        <li class="contact-item">
          <svg class="contact-icon" viewBox="0 0 24 24" aria-hidden="true"><path d="M6.6 10.8a15.1 15.1 0 0 0 6.6 6.6l2.2-2.2a1 1 0 0 1 1-.25 11.4 11.4 0 0 0 3.6.57 1 1 0 0 1 1 1V20a1 1 0 0 1-1 1A17 17 0 0 1 3 4a1 1 0 0 1 1-1h3.5a1 1 0 0 1 1 1c0 1.25.2 2.45.57 3.57a1 1 0 0 1-.25 1z"/></svg>
          <span>+123 555 0147</span>
        </li>
        <li class="contact-item">
          <svg class="contact-icon" viewBox="0 0 24 24" aria-hidden="true"><path d="M8 2h8a2 2 0 0 1 2 2v16a2 2 0 0 1-2 2H8a2 2 0 0 1-2-2V4a2 2 0 0 1 2-2zm0 3v12h8V5zm4 13.5a1 1 0 1 0 0 2 1 1 0 0 0 0-2z"/></svg>
          <span>+111 555 0193</span>
        </li>
        <li class="contact-item">
          <svg class="contact-icon" viewBox="0 0 24 24" aria-hidden="true"><path d="M2 5h20v14H2zm2 2v.5l8 5 8-5V7l-8 5z"/></svg>
          <span>marcusdale@mail.com</span>
        </li>
      </ul>
    </div>
  </section>
</main>
</body>
</html>
```